WEB HOSTING COMPANY WHMCS THEME

The name of the web host company is "brisk maple" so i would like something professional and simple. Il let you guys chouse the colors use your imagination on this, i will need a logo and a business card design. I would also like the theme coded and installed to my whims server and last thing we need to setup the website to go live at te end i will pay extra for that. Thank you

Target Market(s)

Web Hosting Company

Contact Information for Business Card

BRISKMAPLE

Logo Text

BRISKMAPLE

Coding

Coded - Design and coding required

Number of Pages Required

5+ page

Font styles to use
Sans Serif

Requirements
Must have
• EMAIL PHONE NUMBER MOBILE NUMBER WEBSITE AND BUSINESS ADRESS

```html
<!DOCTYPE html>
<html lang="en">
<head>
<meta charset="utf-8">
<title>brisk maple – Web Hosting</title>
<link rel="stylesheet" href="https://fonts.googleapis.com/css2?family=Open+Sans:wght@400;600;700;800&display=swap">
<style>
:root{
  --navy:#1f2a4d;
  --navy-dark:#18213d;
  --slate:#454e6b;
  --green:#5c9e12;
  --green-bright:#6fb31a;
  --grey-bg:#ededed;
  --grey-card:#ececec;
  --line:#d8d8d8;
  --text:#666;
  --ink:#1c2340;
  --white:#fff;
}
*{box-sizing:border-box;margin:0;padding:0}
html,body{width:1200px;height:3689px;overflow:hidden}
body{font-family:"Open Sans",Arial,sans-serif;color:var(--text);background:var(--white);position:relative}
.abs{position:absolute}
p{font-size:12px;line-height:19px}

/* header + hero */
.hero{position:absolute;left:0;top:0;width:1200px;height:615px;background:radial-gradient(ellipse at 50% 40%,#f6f6f6 0%,#e6e6e6 80%)}
.logo{left:133px;top:30px;font-size:31px;font-weight:600;color:var(--green);display:flex;align-items:center;gap:8px;letter-spacing:-.5px}
.logo .mark{width:14px;height:14px;border:3px solid var(--green);border-radius:50%}
.nav{left:488px;top:40px;display:flex;align-items:center;font-size:13px;color:var(--ink)}
.nav a{text-decoration:none;color:var(--ink);margin-right:36px}
.nav a.active{color:var(--green);border-bottom:2px solid var(--green);padding-bottom:4px}
.btn-login{background:var(--navy);color:var(--white);font-size:12px;padding:9px 18px;border-radius:2px;margin-left:-8px}
.hero-kicker{left:133px;top:228px;font-size:16px;color:var(--ink)}
.hero-title{left:133px;top:248px;font-size:31px;font-weight:700;color:var(--ink)}
.hero-text{left:133px;top:292px;width:330px;color:#444}
.hero-list{left:133px;top:358px;list-style:none;font-size:12px;color:#444}
.hero-list li{margin-bottom:11px;display:flex;align-items:center;gap:10px}
.hero-list li::before{content:"";width:11px;height:11px;border-radius:50%;background:#555}
.btn-navy{background:var(--navy);color:var(--white);font-size:12px;display:flex;align-items:center;justify-content:center;border-radius:2px}
.hero-btn{left:133px;top:428px;width:96px;height:34px}
.hero-art{left:490px;top:240px;width:595px;height:375px;background:linear-gradient(135deg,#dfe3ea 0%,#b8c4d6 45%,#5d9ee8 100%);border-radius:6px 6px 0 0}
.arrow{top:292px;width:20px;height:30px}

/* section headers */
.sec-head{position:absolute;left:133px;width:934px;height:135px;border-bottom:1px solid var(--line)}
.sec-head h2{position:absolute;left:0;top:50px;font-size:31px;font-weight:700;color:var(--green)}
.sec-head .divider{position:absolute;left:465px;top:0;width:1px;height:135px;background:var(--line)}
.sec-head p{position:absolute;left:492px;top:38px;width:442px;font-size:11.5px;line-height:19px;color:#888}

/* services */
.service{position:absolute;top:792px;width:290px;height:84px}
.service .icon{position:absolute;left:0;top:0;width:84px;height:84px;background:var(--navy);display:flex;align-items:center;justify-content:center}
.service h3{position:absolute;left:96px;top:0;font-size:18px;font-weight:700;color:var(--ink)}
.service p{position:absolute;left:96px;top:28px;width:190px;font-size:10px;line-height:15px;color:#888}

/* domain */
.domain{position:absolute;left:0;top:954px;width:1200px;height:362px;background:var(--grey-bg)}
.domain h2{left:133px;top:52px;font-size:32px;line-height:40px;font-weight:700;color:var(--ink)}
.domain-input{left:133px;top:158px;width:507px;height:32px;border-bottom:1px solid #bbb;font-size:14px;color:#555;padding-top:4px}
.tlds{left:133px;top:224px;display:flex;font-size:14px;color:#555}
.tlds span{width:96px;display:flex;align-items:center;gap:7px}
.tlds span::before{content:"";width:9px;height:9px;border-radius:50%;border:1px solid #999}
.tlds span.on::before{background:var(--green);border-color:var(--green)}
.domain-btn{left:133px;top:278px;width:88px;height:37px}
.domain-art{left:738px;top:30px;width:332px;height:296px;border-radius:50%;background:radial-gradient(circle at 60% 40%,#f0532b 0%,#e8472a 55%,#3b4a6b 100%)}

/* pricing */
.card{position:absolute;text-align:center}
.card.grey{top:1576px;width:300px;height:322px;background:var(--grey-card)}
.card.feature{top:1557px;left:433px;width:334px;height:356px;background:var(--slate);color:var(--white)}
.card .icon{position:absolute;left:50%;margin-left:-40px;top:-40px;width:80px;height:80px;background:var(--navy);display:flex;align-items:center;justify-content:center}
.card .from{font-size:15px;color:#888}
.card.feature .from{color:#dfe1ea}
.card .price{font-size:46px;font-weight:800;color:var(--green);line-height:52px}
.card.feature .price{color:var(--white)}
.card h3{font-size:20px;font-weight:700;color:var(--ink)}
.card.feature h3{color:var(--white)}
.card p{font-size:11px;line-height:17px;color:#888;width:220px;margin:8px auto 0}
.card.feature p{color:#dfe1ea}
.btn-order{display:inline-flex;align-items:center;gap:6px;border:1px solid #666;background:var(--white);color:#333;font-size:12px;padding:7px 14px;margin-top:20px}
.card.feature .btn-order{background:transparent;border-color:#cfd2dc;color:var(--white)}

/* feedback */
.feedback{position:absolute;left:0;top:1992px;width:1200px;height:644px;background:#efefef}
.photo{position:absolute;top:2208px;width:160px;height:160px}
.quote{left:133px;top:2417px;width:934px;height:136px;background:var(--white);padding:38px 24px 0;font-size:12px;line-height:19px;color:#666}
.quote-notch{left:304px;top:2395px;width:0;height:0;border-left:22px solid transparent;border-right:22px solid transparent;border-bottom:22px solid var(--white)}

/* included */
.feature-item{position:absolute;top:2860px;width:300px;text-align:center}
.feature-item h3{font-size:19px;font-weight:700;color:var(--ink);margin-top:22px}
.feature-item p{font-size:10.5px;line-height:16px;color:#888;width:250px;margin:8px auto 0}

/* newsletter + footer */
.footer{position:absolute;left:0;top:3209px;width:1200px;height:393px;background:var(--navy)}
.newsletter{left:133px;top:3135px;width:934px;height:155px;background:#ebebeb}
.newsletter h2{position:absolute;left:39px;top:36px;font-size:29px;line-height:36px;font-weight:700;color:var(--green)}
.newsletter .email{position:absolute;left:349px;top:52px;width:428px;height:30px;border-bottom:1px solid #bbb;font-size:14px;color:#666}
.newsletter .btn-navy{position:absolute;left:804px;top:50px;width:86px;height:34px}
.foot-col h4{font-size:18px;font-weight:700;color:var(--white)}
.about p{width:310px;font-size:10.5px;line-height:17px;color:#aeb3c6;margin-top:12px}
.about .more{font-size:11px;color:var(--white);font-weight:600;margin-top:10px}
.links ul{list-style:none;margin-top:10px}
.links li{font-size:12px;color:#dde0ea;line-height:27.5px}
.links li::before{content:"• "}
.contact-bar{width:241px;height:34px;background:var(--green);color:var(--white);font-size:12px;display:flex;align-items:center;gap:10px;padding-left:18px;margin-top:6px}
.contact .bars{margin-top:8px}
.socials{display:flex;gap:22px;margin-top:22px;padding-left:10px}
.socials span{width:12px;height:12px;border-radius:50%;background:#dfe2ea}
.server-art{left:0;top:3480px;width:118px;height:209px;background:linear-gradient(180deg,#5e6d8e 0%,#3d5b8f 60%,#5da9e9 100%)}
.bottom-bar{left:0;top:3602px;width:1200px;height:87px;background:var(--navy-dark)}
.copyright{left:184px;top:3632px;font-size:11px;color:#cfd3df}
.pay{top:3635px;width:22px;height:16px;border-radius:2px;background:#d9dbe2}
.pay.round{width:20px;height:20px;border-radius:50%;top:3633px;background:#e9a53a}
.to-top{left:1109px;top:3582px;width:50px;height:50px;border-radius:50%;background:var(--green-bright);display:flex;align-items:center;justify-content:center}
</style>
</head>
<body>

<section class="hero" aria-label="Hero"></section>
<div class="abs hero-art" role="img" aria-label="Illustration of server racks, clouds, a monitor and gear icons"></div>
<div class="abs logo"><span>brisk maple</span><span class="mark"></span></div>
<nav class="abs nav">
  <a class="active">Home</a><a>Hosting</a><a>Domain</a><a>Pricing</a><a>Support</a><a>Customer Care</a>
  <span class="btn-login">&#128274; Login</span>
</nav>
<svg class="abs arrow" style="left:22px" viewBox="0 0 20 30"><path d="M14 4 L5 15 L14 26" fill="none" stroke="#999" stroke-width="2.5"/></svg>
<svg class="abs arrow" style="left:1158px" viewBox="0 0 20 30"><path d="M6 4 L15 15 L6 26" fill="none" stroke="#999" stroke-width="2.5"/></svg>
<div class="abs hero-kicker">Suspendisse</div>
<h1 class="abs hero-title">Tincidunt</h1>
<p class="abs hero-text">Maecenas facilisis non turpis a iaculis. Curabitur tincidunt, metus viverra sodales vestibulum, nisl ante tempor orci, nec sagittis leo ex quis leo.</p>
<ul class="abs hero-list"><li>Nunc ut libero vitae ligula pulvinar aliquam</li><li>Mauris auctor sodales eros vel condimentum</li></ul>
<div class="abs btn-navy hero-btn">Learn More</div>

<div class="sec-head" style="top:615px">
  <h2>Our Services</h2><span class="divider"></span>
  <p>Maecenas facilisis non turpis a iaculis. Curabitur tincidunt, metus viverra sodales vestibulum, nisl ante tempor orci, nec sagittis leo ex quis leo. Donec viverra euismod metus nec ullamcorper.</p>
</div>
<div class="service" style="left:133px">
  <div class="icon"><svg width="38" height="34" viewBox="0 0 38 34" fill="#fff"><rect x="14" y="0" width="10" height="9"/><rect x="0" y="24" width="10" height="9"/><rect x="14" y="24" width="10" height="9"/><rect x="28" y="24" width="10" height="9"/><path d="M18 9v8M5 24v-7h28v7M19 17v7" stroke="#fff" stroke-width="2" fill="none"/></svg></div>
  <h3>Shared Hosting</h3><p>Pellentesque elit neque, bibendum vel turpis eu, laoreet interdum urna. Morbi eleifend sollicitudin semper.</p>
</div>
<div class="service" style="left:460px">
  <div class="icon"><svg width="40" height="26" viewBox="0 0 40 26"><path d="M10 26a9 9 0 0 1-1-18 11 11 0 0 1 21 2 8 8 0 0 1 0 16z" fill="#fff"/></svg></div>
  <h3>Cloud Hosting</h3><p>Pellentesque elit neque, bibendum vel turpis eu, laoreet interdum urna. Morbi eleifend sollicitudin semper.</p>
</div>
<div class="service" style="left:782px">
  <div class="icon"><svg width="30" height="36" viewBox="0 0 30 36" fill="#fff"><ellipse cx="15" cy="5" rx="15" ry="5"/><path d="M0 9c0 3 7 5 15 5s15-2 15-5v7c0 3-7 5-15 5S0 19 0 16zM0 20c0 3 7 5 15 5s15-2 15-5v11c0 3-7 5-15 5S0 34 0 31z"/></svg></div>
  <h3>Dedicated Hosting</h3><p>Pellentesque elit neque, bibendum vel turpis eu, laoreet interdum urna. Morbi eleifend sollicitudin semper.</p>
</div>

<section class="domain" aria-label="Domain search">
  <h2 class="abs">Maecenas facilisis turpis .iaculis<br>Quisque mollis tellus</h2>
  <div class="abs domain-input">eg.example</div>
  <div class="abs tlds"><span class="on">.com</span><span>.net</span><span>.org</span><span>.info</span><span>.biz</span><span>.us</span></div>
  <div class="abs btn-navy domain-btn">&#128269;&nbsp;Search</div>
  <div class="abs domain-art" role="img" aria-label="Illustration of a server rack, database, rocket and tools on an orange circle"></div>
</section>

<div class="sec-head" style="top:1316px">
  <h2>Our Pricing</h2><span class="divider"></span>
  <p>Maecenas facilisis non turpis a iaculis. Curabitur tincidunt, metus viverra sodales vestibulum, nisl ante tempor orci, nec sagittis leo ex quis leo. Donec viverra euismod metus nec ullamcorper.</p>
</div>
<div class="card grey" style="left:133px">
  <div class="icon"><svg width="34" height="30" viewBox="0 0 38 34" fill="#fff"><rect x="14" y="0" width="10" height="9"/><rect x="0" y="24" width="10" height="9"/><rect x="14" y="24" width="10" height="9"/><rect x="28" y="24" width="10" height="9"/><path d="M18 9v8M5 24v-7h28v7M19 17v7" stroke="#fff" stroke-width="2" fill="none"/></svg></div>
  <div style="height:80px"></div>
  <div class="from">Starting At</div><div class="price">$00.00</div><h3>Shared Hosting</h3>
  <p>Curabitur tincidunt, metus viverra sodales vestibulum, nisl ante tempo</p>
  <span class="btn-order">&#128722; Order Now</span>
</div>
<div class="card feature">
  <div class="icon"><svg width="36" height="24" viewBox="0 0 40 26"><path d="M10 26a9 9 0 0 1-1-18 11 11 0 0 1 21 2 8 8 0 0 1 0 16z" fill="#fff"/></svg></div>
  <div style="height:99px"></div>
  <div class="from">Starting At</div><div class="price">$00.00</div><h3>Cloud Hosting</h3>
  <p>Curabitur tincidunt, metus viverra sodales vestibulum, nisl ante tempo</p>
  <span class="btn-order">&#128722; Order Now</span>
</div>
<div class="card grey" style="left:767px">
  <div class="icon"><svg width="26" height="32" viewBox="0 0 30 36" fill="#fff"><ellipse cx="15" cy="5" rx="15" ry="5"/><path d="M0 9c0 3 7 5 15 5s15-2 15-5v7c0 3-7 5-15 5S0 19 0 16zM0 20c0 3 7 5 15 5s15-2 15-5v11c0 3-7 5-15 5S0 34 0 31z"/></svg></div>
  <div style="height:80px"></div>
  <div class="from">Starting At</div><div class="price">$00.00</div><h3>Dedicated Hosting</h3>
  <p>Curabitur tincidunt, metus viverra sodales vestibulum, nisl ante tempo</p>
  <span class="btn-order">&#128722; Order Now</span>
</div>

<section class="feedback" aria-label="Clients feedback"></section>
<div class="sec-head" style="top:1992px">
  <h2>Clients Feedback</h2><span class="divider"></span>
  <p>Maecenas facilisis non turpis a iaculis. Curabitur tincidunt, metus viverra sodales vestibulum, nisl ante tempor orci, nec sagittis leo ex quis leo. Donec viverra euismod metus nec ullamcorper.</p>
</div>
<div class="photo" style="left:243px;background:linear-gradient(180deg,#c9c4bd,#6e6258)" role="img" aria-label="Portrait photo of a client"></div>
<div class="photo" style="left:428px;background:linear-gradient(180deg,#c4a88e,#7b5a44)" role="img" aria-label="Portrait photo of a client"></div>
<div class="photo" style="left:610px;background:linear-gradient(180deg,#cfc9c2,#5f5750)" role="img" aria-label="Portrait photo of a client"></div>
<div class="photo" style="left:794px;background:linear-gradient(180deg,#b99a84,#6b4a3a)" role="img" aria-label="Portrait photo of a client"></div>
<div class="abs quote-notch"></div>
<p class="abs quote">Aenean nec ex in urna congue bibendum at dictum justo. Donec quis elementum tellus. Cras in lacus dignissim, consequat dolor in, ullamcorper dui. Fusce augue massa, tempus hendrerit ultricies eget, maximus eu nisl. Suspendisse tempor, diam eget iaculis ullamcorper, ipsum metus placerat tortor, in consectetur massa purus eget ligula.</p>

<div class="sec-head" style="top:2636px">
  <h2>Services Included</h2><span class="divider"></span>
  <p>Maecenas facilisis non turpis a iaculis. Curabitur tincidunt, metus viverra sodales vestibulum, nisl ante tempor orci, nec sagittis leo ex quis leo. Donec viverra euismod metus nec ullamcorper.</p>
</div>
<div class="feature-item" style="left:120px">
  <svg width="84" height="84" viewBox="0 0 84 84"><circle cx="42" cy="42" r="40" fill="#5aa86a"/><circle cx="42" cy="42" r="27" fill="#eaf4ec"/><circle cx="42" cy="42" r="16" fill="#5aa86a"/><path d="M12 28h16M56 56h16M28 12v16M56 72V56" stroke="#fff" stroke-width="6"/></svg>
  <h3>24/7 Support</h3><p>Nullam dignissim ullamcorper ligula eget fermentum. Pellentesque elit tortor, consectetur sit amet urna in, molestie sodales urna.</p>
</div>
<div class="feature-item" style="left:452px">
  <svg width="84" height="84" viewBox="0 0 84 84"><rect x="14" y="6" width="56" height="18" rx="2" fill="#8fcf9a"/><rect x="14" y="30" width="56" height="18" rx="2" fill="#5aa86a"/><rect x="24" y="13" width="22" height="4" fill="#fff"/><rect x="24" y="37" width="22" height="4" fill="#fff"/><path d="M42 48v18M14 70h56" stroke="#5aa86a" stroke-width="4"/><circle cx="42" cy="70" r="7" fill="#8fcf9a"/></svg>
  <h3>45 Day Guarantee</h3><p>Nullam dignissim ullamcorper ligula eget fermentum. Pellentesque elit tortor, consectetur sit amet urna in, molestie sodales urna.</p>
</div>
<div class="feature-item" style="left:794px">
  <svg width="84" height="84" viewBox="0 0 84 84"><rect x="6" y="10" width="72" height="56" rx="3" fill="#5aa86a"/><rect x="6" y="10" width="72" height="10" fill="#8fcf9a"/><path d="M14 56 L30 34 L42 46 L54 30 L70 56z" fill="#eaf4ec"/></svg>
  <h3>99.9% Uptime</h3><p>Nullam dignissim ullamcorper ligula eget fermentum. Pellentesque elit tortor, consectetur sit amet urna in, molestie sodales urna.</p>
</div>

<footer class="footer" aria-label="Footer"></footer>
<div class="abs server-art" role="img" aria-label="Illustration of a server rack with a cloud"></div>
<div class="abs newsletter">
  <h2>Subscribe To Our<br>Newsletter</h2>
  <div class="email">Email Address</div>
  <div class="btn-navy">Subscribe</div>
</div>
<div class="abs foot-col about" style="left:133px;top:3352px">
  <h4>About Us</h4>
  <p>Nulla iaculis et ipsum eu volutpat. Etiam iaculis, erat vitae efficitur dictum, velit diam pellentesque mauris, vel fringilla sapien ante eu augue. Etiam id tincidunt nisi, condimentum purus quam. Morbi a commodo turpis. Etiam hendrerit tortor, a feugiat lectus. Pellentesque dictum dolor molestie. Donec lacinia sed augue sit amet efficitur. Nunc nulla diam, iaculis a dolor vel, mattis fermentum ex.</p>
  <div class="more">Read more</div>
</div>
<div class="abs foot-col links" style="left:558px;top:3352px">
  <h4>Useful Links</h4>
  <ul><li>Home</li><li>Hosting</li><li>Domain</li><li>Pricing</li><li>Support</li><li>Customer Care</li></ul>
</div>
<div class="abs foot-col contact" style="left:826px;top:3352px">
  <h4>Contact</h4>
  <div class="bars">
    <div class="contact-bar">&#128172; Live Chat</div>
    <div class="contact-bar">&#128222; 555 014 2290</div>
    <div class="contact-bar">&#9993; info@briskmaple.com</div>
  </div>
  <div class="socials"><span></span><span></span><span></span><span></span></div>
</div>
<div class="abs bottom-bar"></div>
<div class="abs copyright">Copyright © 2017 Company name. All rights reserved</div>
<span class="abs pay round" style="left:862px"></span>
<span class="abs pay round" style="left:888px;background:#c8ccd6"></span>
<span class="abs pay" style="left:916px"></span>
<span class="abs pay" style="left:944px"></span>
<span class="abs pay" style="left:972px"></span>
<span class="abs pay" style="left:1000px"></span>
<span class="abs pay" style="left:1028px"></span>
<div class="abs to-top"><svg width="22" height="14" viewBox="0 0 22 14"><path d="M2 12 L11 3 L20 12" fill="none" stroke="#fff" stroke-width="4"/></svg></div>

</body>
</html>
```